Stationary Package for Construction Company
Modern and Professional
Stationary Package for Construction Company - Construction
Creative Brief
Professional
Karl T. Wentworth
V.P., Operations & Sr. Project Manager
7148 Orchard Lane, Unit 512 Myrtle Beach, SC 29614
843.555.0178 ext. 214
Karl@BrimstackLLC.example
www.BrimstackLLC.example
Current logo is uploaded in .ai format. If color needs to be altered, that is ok. We may also need an alternate color for back of business card. I have also uploaded a few card samples that we already like.
Back of card should be alternate color, either red or black. Two options: One card back with logo only, and one version with logo, web address and services rendered, which I'll specify in greater detail as we narrow down specific designs that we like.

```html
<!DOCTYPE html>
<html lang="en">
<head>
<meta charset="utf-8">
<title>Brimstack Construction Business Card</title>
<link href="https://fonts.googleapis.com/css2?family=Archivo+Black&family=Roboto:wght@400;500;700&display=swap" rel="stylesheet">
<style>
  :root {
    --bg: #7a7a7a;
    --brick: #9e2d1f;
    --brick-dark: #6e1c12;
    --brand-red: #e3232a;
    --ink: #1c1c1c;
    --paper: #ffffff;
    --muted: #4a4a4a;
  }
  * { box-sizing: border-box; margin: 0; padding: 0; }
  html, body { width: 1200px; height: 908px; overflow: hidden; }
  body {
    background: var(--bg);
    font-family: "Roboto", Arial, sans-serif;
    position: relative;
  }
  .card {
    position: absolute;
    top: 299px;
    width: 540px;
    height: 310px;
    border-radius: 22px;
    overflow: hidden;
    box-shadow: 0 10px 28px rgba(0,0,0,.35);
  }
  .card--back { left: 40px; }
  .card--front { left: 620px; background: var(--paper); }

  .brick-field {
    position: absolute; inset: 0;
    background: radial-gradient(ellipse at 35% 30%, #b8402c 0%, var(--brick) 45%, var(--brick-dark) 100%);
  }
  .wordmark {
    position: absolute;
    font-family: "Archivo Black", "Arial Black", sans-serif;
    line-height: .95;
    text-transform: uppercase;
  }
  .card--back .wordmark {
    left: 0; right: 0; top: 92px;
    text-align: center;
    color: var(--paper);
    font-size: 36px;
  }
  .tag-script {
    position: absolute;
    font-size: 12px;
    font-style: italic;
    letter-spacing: .5px;
  }
  .card--back .tag-script {
    left: 0; right: 0; top: 176px; text-align: center; color: var(--paper);
  }
  .motto {
    position: absolute;
    font-family: "Archivo Black", "Arial Black", sans-serif;
    text-transform: uppercase;
    letter-spacing: 1px;
  }
  .card--back .motto {
    left: 0; right: 0; top: 198px; text-align: center; color: var(--paper); font-size: 17px;
  }

  .swoosh { position: absolute; inset: 0; }
  .card--front .wordmark {
    left: 30px; top: 40px; color: var(--brand-red); font-size: 26px;
  }
  .card--front .tag-script { left: 30px; top: 98px; color: var(--brand-red); font-size: 10px; }
  .card--front .motto { left: 30px; top: 116px; color: var(--brand-red); font-size: 14px; }

  .contact {
    position: absolute; left: 292px; top: 34px;
    list-style: none; font-size: 11.5px; color: var(--ink);
  }
  .contact li { display: flex; align-items: center; gap: 7px; height: 18px; white-space: nowrap; }
  .contact .plain { padding-left: 21px; }
  .contact svg { width: 14px; height: 14px; flex: none; }

  .person { position: absolute; left: 30px; top: 196px; }
  .person__name { font-size: 19px; font-weight: 500; color: var(--ink); }
  .person__title { font-size: 12.5px; color: var(--brand-red); margin-top: 4px; line-height: 1.35; }
</style>
</head>
<body>

<section class="card card--back">
  <div class="brick-field" role="img" aria-label="Red brick wall texture"></div>
  <div class="wordmark">Brimstack<br>Construction</div>
  <div class="tag-script">Full Service Build Company</div>
  <div class="motto">Quality · Service · Price</div>
</section>

<section class="card card--front">
  <svg class="swoosh" viewBox="0 0 540 310" preserveAspectRatio="none" aria-hidden="true">
    <path d="M478 0 H540 V80 C532 42 512 14 478 0 Z" fill="var(--ink)"/>
    <path d="M462 0 H478 C512 14 532 42 540 80 V100 C530 52 506 16 462 0 Z" fill="var(--brand-red)"/>
    <path d="M0 270 C140 300 360 300 540 250 V310 H0 Z" fill="var(--ink)"/>
    <path d="M0 258 C140 290 360 290 540 238 V250 C360 300 140 300 0 270 Z" fill="var(--brand-red)"/>
  </svg>

  <div class="wordmark">Brimstack<br>Construction</div>
  <div class="tag-script">Full Service Build Company</div>
  <div class="motto">Quality · Service · Price</div>

  <ul class="contact">
    <li>
      <svg viewBox="0 0 14 14"><circle cx="7" cy="7" r="7" fill="var(--brand-red)"/><path d="M7 3.2a2.4 2.4 0 0 0-2.4 2.4C4.6 7.5 7 10.8 7 10.8s2.4-3.3 2.4-5.2A2.4 2.4 0 0 0 7 3.2z" fill="#fff"/></svg>
      7148 Orchard Lane, Unit 512
    </li>
    <li class="plain">Myrtle Beach, SC 29614</li>
    <li>
      <svg viewBox="0 0 14 14"><circle cx="7" cy="7" r="7" fill="var(--brand-red)"/><path d="M4.5 3.5l1.6 1.8-.8 1.1a5 5 0 0 0 2.3 2.3l1.1-.8 1.8 1.6-.9 1.1C7 10.4 3.6 7 3.4 4.4z" fill="#fff"/></svg>
      843.555.0178 ext. 214
    </li>
    <li>
      <svg viewBox="0 0 14 14"><circle cx="7" cy="7" r="7" fill="var(--brand-red)"/><rect x="5" y="3" width="4" height="8" rx="1" fill="#fff"/></svg>
      843.555.0199
    </li>
    <li>
      <svg viewBox="0 0 14 14"><circle cx="7" cy="7" r="7" fill="var(--brand-red)"/><rect x="4" y="5" width="6" height="4.5" fill="#fff"/><rect x="5" y="3" width="4" height="2" fill="#fff"/></svg>
      866.555.0142
    </li>
    <li>
      <svg viewBox="0 0 14 14"><circle cx="7" cy="7" r="7" fill="var(--brand-red)"/><rect x="3.5" y="4.5" width="7" height="5" fill="#fff"/><path d="M3.5 4.5L7 7.3l3.5-2.8" stroke="var(--brand-red)" stroke-width=".8" fill="none"/></svg>
      Karl@BrimstackLLC.example
    </li>
    <li>
      <svg viewBox="0 0 14 14"><circle cx="7" cy="7" r="7" fill="var(--brand-red)"/><circle cx="7" cy="7" r="3.4" stroke="#fff" stroke-width="1" fill="none"/><path d="M3.6 7h6.8M7 3.6v6.8" stroke="#fff" stroke-width=".8"/></svg>
      www.BrimstackLLC.example
    </li>
  </ul>

  <div class="person">
    <div class="person__name">Karl T. Wentworth</div>
    <div class="person__title">V.P., Operations &amp;<br>Sr. Project Manager</div>
  </div>
</section>

</body>
</html>
```